A modern and fresh looking church website

St Maren’s is looking for a new site design for their church. The church is a part of a group of the ‘Calverin Church’ Australia and needs to kind of tie into their branding within reason.
This means, we would need to use the logo colours (Blue, Gold, Red) throughout the website and the design needs to be fresh, modern, clean, and mobile-friendly. The front page must have the following as features:
• Sermons (Podcasts and Videos)
• Events
• Venue Hire (Weddings)
The website will be mainly information-based and will have a few forms. From our recent engagement with the church, I did draft up a mock-up design for them and even it looks better than their current site, it’s not giving a ‘stand out impression’ and has that out of date look.
The inner pages will be based off the front-page design so we will take care of that, we are just looking for a front-page design that is unique and has the wow factor.
The website will be coded by our in-house development team and will be coded in a WordPress format using Elementor pro.
We are looking for a couple of designers to design 1-3 mock-ups by taking our current draft and putting their spin to it.
Hi,
Due to Christmas and the client was on leave, the design selection has been delayed. It was not ideal as I knew this would happen.
I made contact with the client and just been told that the client is leaving the church and a handover is happening for the new staff member. The new staff member will present all designs to the board for selection. This is due to be completed by the first week of February 2021.
We thanks for your patients as this was not expected and we seeing if we can hurry this process up.

```html
<!DOCTYPE html>
<html lang="en">
<head>
<meta charset="utf-8">
<title>St Maren’s Perth Calverin Church</title>
<link href="https://fonts.googleapis.com/css2?family=Archivo:wght@500;600;700&family=Montserrat:wght@400;500;600;700&family=Roboto+Condensed:wght@300&display=swap" rel="stylesheet">
<style>
:root{
  --red:#e5262a;
  --blue:#1c5bab;
  --navy:#13264f;
  --gold:#f3a33a;
  --ink:#1b1b1b;
  --text:#555;
  --grey:#ececec;
  --white:#fff;
}
*{box-sizing:border-box;margin:0;padding:0}
html,body{width:1200px;height:5314px;overflow:hidden}
body{font-family:"Montserrat",sans-serif;color:var(--text);background:var(--white);position:relative}
h1,h2,h3{font-family:"Archivo",sans-serif;color:var(--ink);font-weight:600}
.btn{display:inline-block;background:var(--red);color:#fff;font:700 15px "Montserrat",sans-serif;padding:11px 20px;border-radius:3px;text-transform:uppercase}
.btn--blue{background:var(--blue)}
.eyebrow{font:500 21px "Montserrat",sans-serif;color:var(--gold);text-transform:uppercase}
.wrap{position:absolute;left:99px;width:1002px}

/* top bar */
.topbar{position:absolute;top:0;left:0;width:1200px;height:41px;background:var(--red);color:#fff;font-size:13px;display:flex;align-items:center;padding:0 99px;justify-content:space-between}
.topbar a{color:#fff;text-decoration:underline;font-weight:600;margin-left:10px}
.topbar .right{display:flex;align-items:center;gap:10px}
.dot{width:26px;height:26px;border:2px solid #fff;border-radius:50%;display:inline-block}
.sep{width:1px;height:30px;background:rgba(255,255,255,.6);margin:0 6px}

/* header */
.header{position:absolute;top:41px;left:0;width:1200px;height:79px;display:flex;align-items:center;justify-content:space-between;padding:0 99px}
.brand{display:flex;align-items:center;gap:12px;font:700 26px "Archivo",sans-serif;color:var(--blue)}
.brand-mark{width:44px;height:44px;border-radius:50%;background:var(--blue)}
.contact{display:flex;gap:24px;align-items:center}
.phone{display:flex;align-items:center;gap:10px}
.phone-icon{width:38px;height:38px;border-radius:50%;background:var(--blue);display:flex;align-items:center;justify-content:center}
.phone small,.services small{display:block;color:var(--blue);font-size:13px;font-weight:600}
.phone b{font-size:19px;color:var(--ink);font-weight:600}
.services{font-size:11.5px;color:var(--ink);line-height:1.35}
.services small{font-size:14px}

/* nav */
.nav{position:absolute;top:120px;left:0;width:1200px;height:43px;background:var(--blue);display:flex;padding:0 77px}
.nav a{color:#fff;font:600 14px "Montserrat",sans-serif;display:flex;align-items:center;padding:0 24px;margin-right:38px;text-transform:uppercase}
.nav a.active{background:var(--red)}

/* hero */
.hero{position:absolute;top:163px;left:0;width:1200px;height:581px;background:linear-gradient(180deg,#6b5a4e 0%,#8d6b63 40%,#4a3b3a 100%);text-align:center;color:#fff}
.hero-text{position:absolute;top:340px;left:0;width:100%}
.hero-text .kicker{font:300 31px "Roboto Condensed",sans-serif}
.hero-text h1{color:#fff;font-size:43px;font-weight:600;margin-top:4px}
.hero-text p{font-size:15px;margin-top:12px}
.scroll{position:absolute;left:590px;top:524px}

/* covid */
.notice{position:absolute;top:744px;left:0;width:1200px;height:101px;background:var(--red);color:#fff;display:flex;align-items:center;padding-left:174px;gap:28px}
.notice h3{color:#fff;font:500 17px "Montserrat",sans-serif}
.notice p{font-size:11.5px;line-height:1.5;width:780px;margin-top:3px}

/* welcome */
.welcome{position:absolute;top:845px;left:0;width:1200px;height:640px}
.welcome .copy{position:absolute;left:99px;top:118px;width:480px}
.welcome h2{font-size:37px;line-height:1.13;margin-top:4px}
.rule{width:66px;height:4px;background:var(--blue);margin:14px 0 18px}
.welcome p{font-size:13.5px;line-height:1.8;margin-bottom:10px}
.welcome .btn{margin-top:10px}
.ph-a{position:absolute;left:633px;top:138px;width:322px;height:276px;border-radius:14px 80px 14px 14px;background:linear-gradient(180deg,#3a6aa5,#bcd2e6 60%,#1c1c1c 90%)}
.ph-b{position:absolute;left:826px;top:305px;width:218px;height:188px;border:6px solid #fff;border-radius:0 70px 0 0;background:linear-gradient(180deg,#a7c3dc,#6e4a35 60%,#3f2d22);box-shadow:0 4px 16px rgba(0,0,0,.12)}
.sq{position:absolute;left:977px;top:208px;width:46px;height:46px;border:2px solid #bcd0ea;border-radius:6px}

/* features */
.features{position:absolute;top:1485px;left:0;width:1200px;height:1251px;background:var(--grey);border-radius:0 110px 0 110px}
.feature{position:absolute;width:1200px;height:300px}
.feature .img{position:absolute;width:377px;height:302px;border-radius:0 36px 0 36px}
.feature .txt{position:absolute;width:460px}
.feature h2{font-size:37px}
.feature p{font-size:13.5px;line-height:1.8;margin:14px 0 20px}

/* sermons */
.sermons{position:absolute;top:2736px;left:0;width:1200px;height:1027px;text-align:center}
.sec-head h2{font-size:37px;margin-top:6px}
.sec-head p{font-size:13.5px;line-height:1.8;margin:12px auto 0;width:660px}
.player{position:absolute;left:280px;width:640px;height:90px;text-align:left}
.player .meta{position:absolute;left:40px;top:0;font-size:11px;color:#888}
.player .meta b{display:block;font:600 17px "Archivo",sans-serif;color:var(--ink);margin-top:2px}
.note{position:absolute;left:0;top:6px}
.controls{position:absolute;top:50px;left:0;width:640px;height:32px;display:flex;align-items:center;gap:12px;font-size:11px}
.play{width:32px;height:32px;border-radius:50%;background:var(--blue);display:flex;align-items:center;justify-content:center}
.t1{color:var(--gold);width:34px}
.bar{position:relative;width:420px;height:6px;background:#cfd8e6;border-radius:3px}
.bar i{position:absolute;left:0;top:0;height:6px;width:69%;background:var(--blue);border-radius:3px}
.bar em{position:absolute;left:67.5%;top:-3px;width:12px;height:12px;border-radius:50%;background:var(--gold)}
.vol{width:60px;height:6px;background:var(--blue);border-radius:3px}

/* prayer */
.prayer{position:absolute;top:3763px;left:0;width:1200px;height:439px;border-radius:0 110px 0 110px;background:linear-gradient(90deg,#b8284b 0%,#d8653f 35%,#c5488f 65%,#3a1f6e 100%);text-align:center;color:#fff}
.prayer .eyebrow{color:#fde4c6;display:block;margin-top:114px;font-size:19px}
.prayer h2{color:#fff;font-size:37px;margin-top:4px}
.prayer p{font-size:13.5px;line-height:1.8;width:700px;margin:14px auto 20px}
.prayer .btn{margin:0 3px}

/* news */
.news{position:absolute;top:4202px;left:0;width:1200px;height:726px;text-align:center}
.card{position:absolute;top:272px;width:313px;height:381px;text-align:left}
.card .img{height:190px;border-radius:0 60px 0 0}
.card .body{position:absolute;top:148px;left:28px;right:0;height:233px;background:#fff;border-radius:0 40px 0 0;border-bottom:3px solid var(--red);padding:20px 24px}
.card h3{font-size:21px;line-height:1.2}
.card .date{display:flex;align-items:center;gap:8px;font-size:13px;color:var(--ink);font-weight:600;margin:12px 0 10px}
.card .date i{width:14px;height:14px;border-radius:50%;background:var(--red);display:inline-block}
.card p{font-size:13.5px;line-height:1.7}

/* footer */
.footer{position:absolute;top:4928px;left:0;width:1200px;height:386px;background:var(--blue);border-radius:0 110px 0 0;color:#fff}
.footer h4{font:600 15px "Montserrat",sans-serif;text-transform:uppercase;margin-bottom:12px}
.fcol{position:absolute;top:72px;font-size:13.5px;line-height:1.85}
.fcol a{color:#fff;display:block;text-decoration:none}
.fbrand{display:flex;align-items:center;gap:8px;font:700 15px "Archivo",sans-serif;margin-bottom:10px}
.fbrand span{width:36px;height:36px;border-radius:50%;border:2px solid #fff}
.fcol .small{font-size:11.5px;line-height:1.8;width:210px}
.fsocial{display:flex;gap:6px;margin-top:14px}
.fsocial i{width:26px;height:26px;border:2px solid #fff;border-radius:50%}
.input{width:252px;height:40px;background:#fff;border-radius:3px;color:#888;font-size:12px;padding:12px}
.submit{width:252px;height:40px;background:var(--red);border-radius:3px;margin-top:12px;text-align:center;font:700 13px/40px "Montserrat",sans-serif}
.fline{position:absolute;top:318px;left:99px;width:1002px;height:1px;background:rgba(255,255,255,.35)}
.copyright{position:absolute;top:340px;width:100%;text-align:center;font-size:13.5px}
</style>
</head>
<body>

<div class="topbar">
  <div><svg width="22" height="20" viewBox="0 0 22 20" style="vertical-align:middle;margin-right:10px"><path d="M11 2L20.5 18H1.5Z" fill="none" stroke="#fff" stroke-width="2"/><path d="M11 8v5M11 15v1" stroke="#fff" stroke-width="2"/></svg>St Maren’s Response to COVID-19 <a>Read More</a></div>
  <div class="right">
    <svg width="10" height="14" viewBox="0 0 10 14"><path d="M5 0a5 5 0 0 1 5 5c0 4-5 9-5 9S0 9 0 5a5 5 0 0 1 5-5z" fill="#fff"/></svg>
    42 Harlow Street Perth, WA 6000
    <span class="sep"></span><span class="dot"></span><span class="dot"></span><span class="dot"></span>
  </div>
</div>

<header class="header">
  <div class="brand"><span class="brand-mark"></span>St Maren’s</div>
  <div class="contact">
    <div class="phone">
      <span class="phone-icon"><svg width="18" height="18" viewBox="0 0 24 24"><path d="M6.6 10.8a15 15 0 0 0 6.6 6.6l2.2-2.2a1 1 0 0 1 1-.25 11.4 11.4 0 0 0 3.6.57 1 1 0 0 1 1 1V20a1 1 0 0 1-1 1A17 17 0 0 1 3 4a1 1 0 0 1 1-1h3.5a1 1 0 0 1 1 1c0 1.25.2 2.45.57 3.57a1 1 0 0 1-.25 1z" fill="#fff"/></svg></span>
      <div><small>Phone</small><b>08 9000 4417</b></div>
    </div>
    <div class="services"><small>Weekend Services</small>Saturday 6pm Sunday<br>8:30am &amp; 10:20am</div>
  </div>
</header>

<nav class="nav">
  <a class="active">Home</a><a>Sermons</a><a>About Us ⌄</a><a>Achurch Life</a><a>News</a><a>Weddings</a><a>Contact Us</a>
</nav>

<section class="hero" role="img" aria-label="Group photo of the church congregation standing together in the sanctuary">
  <div class="hero-text">
    <div class="kicker">Calverin Church Of Australia</div>
    <h1>Where Love Comes To Life</h1>
    <p>A place where we are learning to see as God sees and love as God loves.</p>
  </div>
  <svg class="scroll" width="20" height="40" viewBox="0 0 20 40"><rect x="3" y="1" width="14" height="22" rx="7" fill="none" stroke="#fff" stroke-width="1.5"/><path d="M10 6v5M5 28l5 4 5-4M5 34l5 4 5-4" fill="none" stroke="#fff" stroke-width="1.5"/></svg>
</section>

<section class="notice">
  <svg width="52" height="46" viewBox="0 0 52 46"><path d="M26 3L49 43H3Z" fill="none" stroke="#fff" stroke-width="3" stroke-linejoin="round"/><path d="M26 17v13M26 35v3" stroke="#fff" stroke-width="3.5"/></svg>
  <div>
    <h3>St Maren’s Response to COVID-19</h3>
    <p>Due to the State Government restrictions, we can only have up to 70 people in each services. To attend one of our worship services, you must book your spot by calling our office or by emailing us.</p>
  </div>
</section>

<section class="welcome">
  <div class="copy">
    <div class="eyebrow" style="text-transform:none">Welcome To</div>
    <h2>St Maren’s Perth Calverin Church</h2>
    <div class="rule"></div>
    <p>Lorem ipsum dolor sit amet, consectetur adi elit eiusmo incnt ut labore et dolore magna aliqua. Quis ipsum susse ultries gida. Risus commodo viverra maecenas acsan lacus vel facilisis. Lorem m dolor sit amet, conr adipiscin elit, sed do eiusmod tempor incidi iore et dolore ma aliqua. Qm suspendisse ultrices gravida.</p>
    <p>Risus commodo viverra mas accums lus vel facilisis. Lom ipsum dolor sit amet, consectetur adng elit, sed do eiusmod tempor incididunt ut laore et e gna aliqua.</p>
    <span class="btn">Read More</span>
  </div>
  <div class="ph-a" role="img" aria-label="Cross silhouette against a bright sky at sunrise"></div>
  <span class="sq"></span>
  <div class="ph-b" role="img" aria-label="Brick church building exterior"></div>
</section>

<section class="features">
  <div class="feature" style="top:120px">
    <div class="img" style="left:157px;background:linear-gradient(135deg,#6b5140,#c49b7c 50%,#4a3a30)" role="img" aria-label="Young adults reading the Bible together on a sofa"></div>
    <div class="txt" style="left:577px;top:26px">
      <h2>Latest Events</h2>
      <p>Lorem ipsum dolor sit amet, consectetur adi elit eiusmo incidunt ut labore et dolore magna aliqua. Quis ipsum sundise ultricesa. Rsus commodo viverra maecnas acsan lacus vel facilisis. Lore lkr t amet, conr adipiscin elit, sed do eiusmod tempor incididunt ut labor mga aliqua. suspendisse ultrices gravida.</p>
      <span class="btn">Read More</span>
    </div>
  </div>
  <div class="feature" style="top:476px">
    <div class="txt" style="left:161px;top:26px">
      <h2>Weddings - Venue Hire</h2>
      <p>Lorem ipsum dolor sit amet, consectetur adi elit eiusmo incidunt ut labore et dolore magna aliqua. Quis ipsum sundise ultricesa. Rsus commodo viverra maecnas acsan lacus vel facilisis. Lore lkr t amet, conr adipiscin elit, sed do eiusmod tempor incididunt ut labor mga aliqua. suspendisse ultrices gravida.</p>
      <span class="btn">Read More</span>
    </div>
    <div class="img" style="left:661px;background:linear-gradient(135deg,#3d4a32,#8a7a66 50%,#5b4438)" role="img" aria-label="Wedding ceremony inside the church beside a Christmas tree"></div>
  </div>
  <div class="feature" style="top:831px">
    <div class="img" style="left:157px;background:linear-gradient(180deg,#7a5a3a,#e0a04a 55%,#3a2414)" role="img" aria-label="Raised hands holding a small cross against a golden sunset"></div>
    <div class="txt" style="left:577px;top:26px">
      <h2>Recent Podcasts &amp; Videos</h2>
      <p>Lorem ipsum dolor sit amet, consectetur adi elit eiusmo incidunt ut labore et dolore magna aliqua. Quis ipsum sundise ultricesa. Rsus commodo viverra maecnas acsan lacus vel facilisis. Lore lkr t amet, conr adipiscin elit, sed do eiusmod tempor incididunt ut labor mga aliqua. suspendisse ultrices gravida.</p>
      <span class="btn">Read More</span>
    </div>
  </div>
</section>

<section class="sermons">
  <div class="sec-head" style="margin-top:132px">
    <div class="eyebrow">Sermon Podcasts</div>
    <h2>Listen To Our Sermons</h2>
    <p>Lorem ipsum dolor sit amet, consectetur adi elit eiusmo incnt ut labore et dolore magna aliqua. Quis ipsum susse ultries gida. Risus commodo viverra maecnas acsan</p>
  </div>

  <div class="player" style="top:284px">
    <svg class="note" width="30" height="34" viewBox="0 0 30 34"><path d="M9 26V6l18-4v20" fill="none" stroke="var(--gold)" stroke-width="2.5"/><circle cx="5" cy="27" r="4.5" fill="none" stroke="var(--gold)" stroke-width="2.5"/><circle cx="23" cy="23" r="4.5" fill="none" stroke="var(--gold)" stroke-width="2.5"/></svg>
    <div class="meta">Sermon by Daniel Marsh<b>March 28 - Lorem ipsum Dolor Sit</b></div>
    <div class="controls"><span class="play"><svg width="12" height="14"><path d="M1 0l11 7-11 7z" fill="#fff"/></svg></span><span class="t1">00:58</span><span class="bar"><i></i><em></em></span><span>00:58</span><svg width="14" height="12"><path d="M0 4h4l5-4v12l-5-4H0z" fill="#444"/></svg><span class="vol"></span></div>
  </div>
  <div class="player" style="top:401px">
    <svg class="note" width="30" height="34" viewBox="0 0 30 34"><path d="M9 26V6l18-4v20" fill="none" stroke="var(--gold)" stroke-width="2.5"/><circle cx="5" cy="27" r="4.5" fill="none" stroke="var(--gold)" stroke-width="2.5"/><circle cx="23" cy="23" r="4.5" fill="none" stroke="var(--gold)" stroke-width="2.5"/></svg>
    <div class="meta">Sermon by Daniel Marsh<b>March 28 - Lorem ipsum Dolor Sit</b></div>
    <div class="controls"><span class="play"><svg width="12" height="14"><path d="M1 0l11 7-11 7z" fill="#fff"/></svg></span><span class="t1">00:58</span><span class="bar"><i></i><em></em></span><span>00:58</span><svg width="14" height="12"><path d="M0 4h4l5-4v12l-5-4H0z" fill="#444"/></svg><span class="vol"></span></div>
  </div>
  <div class="player" style="top:518px">
    <svg class="note" width="30" height="34" viewBox="0 0 30 34"><path d="M9 26V6l18-4v20" fill="none" stroke="var(--gold)" stroke-width="2.5"/><circle cx="5" cy="27" r="4.5" fill="none" stroke="var(--gold)" stroke-width="2.5"/><circle cx="23" cy="23" r="4.5" fill="none" stroke="var(--gold)" stroke-width="2.5"/></svg>
    <div class="meta">Sermon by Daniel Marsh<b>March 28 - Lorem ipsum Dolor Sit</b></div>
    <div class="controls"><span class="play"><svg width="12" height="14"><path d="M1 0l11 7-11 7z" fill="#fff"/></svg></span><span class="t1">00:58</span><span class="bar"><i></i><em></em></span><span>00:58</span><svg width="14" height="12"><path d="M0 4h4l5-4v12l-5-4H0z" fill="#444"/></svg><span class="vol"></span></div>
  </div>
  <div class="player" style="top:635px">
    <svg class="note" width="30" height="34" viewBox="0 0 30 34"><path d="M9 26V6l18-4v20" fill="none" stroke="var(--gold)" stroke-width="2.5"/><circle cx="5" cy="27" r="4.5" fill="none" stroke="var(--gold)" stroke-width="2.5"/><circle cx="23" cy="23" r="4.5" fill="none" stroke="var(--gold)" stroke-width="2.5"/></svg>
    <div class="meta">Sermon by Daniel Marsh<b>March 28 - Lorem ipsum Dolor Sit</b></div>
    <div class="controls"><span class="play"><svg width="12" height="14"><path d="M1 0l11 7-11 7z" fill="#fff"/></svg></span><span class="t1">00:58</span><span class="bar"><i></i><em></em></span><span>00:58</span><svg width="14" height="12"><path d="M0 4h4l5-4v12l-5-4H0z" fill="#444"/></svg><span class="vol"></span></div>
  </div>
  <div class="player" style="top:752px">
    <svg class="note" width="30" height="34" viewBox="0 0 30 34"><path d="M9 26V6l18-4v20" fill="none" stroke="var(--gold)" stroke-width="2.5"/><circle cx="5" cy="27" r="4.5" fill="none" stroke="var(--gold)" stroke-width="2.5"/><circle cx="23" cy="23" r="4.5" fill="none" stroke="var(--gold)" stroke-width="2.5"/></svg>
    <div class="meta">Sermon by Daniel Marsh<b>March 28 - Lorem ipsum Dolor Sit</b></div>
    <div class="controls"><span class="play"><svg width="12" height="14"><path d="M1 0l11 7-11 7z" fill="#fff"/></svg></span><span class="t1">00:58</span><span class="bar"><i></i><em></em></span><span>00:58</span><svg width="14" height="12"><path d="M0 4h4l5-4v12l-5-4H0z" fill="#444"/></svg><span class="vol"></span></div>
  </div>

  <span class="btn" style="position:absolute;top:858px;left:483px;width:234px;font-size:14px">View More Poscasts</span>
</section>

<section class="prayer" role="img" aria-label="Warm blurred light behind a crucifix">
  <span class="eyebrow">Prayer Requests</span>
  <h2>How Can We Pray For You?</h2>
  <p>Lorem ipsum dolor sit amet, consectetur adi elit eiusmo incnt ut labore et dolore magna aliqua. Quis ipsum susse ultries gida. Risus commodo viverra maecnas acsan Lorem ipsum dolor sit amet, consectetur adi elit eiusmo incnt ut labore et dolore magna aliqua.</p>
  <span class="btn btn--blue">Get Started</span><span class="btn">Read More</span>
</section>

<section class="news">
  <div class="sec-head" style="margin-top:134px">
    <div class="eyebrow">News</div>
    <h2>Latest From News</h2>
    <p>Lorem ipsum dolor sit amet, consectetur adi elit eiusmo incnt ut labore et dolore magna aliqua. Quis ipsum susse ultries gida. Risus commodo viverra maecnas acsan</p>
  </div>
  <article class="card" style="left:99px">
    <div class="img" style="background:linear-gradient(180deg,#1a1a1a,#6a2a26 60%,#b23b31)" role="img" aria-label="Choir singing carols in the courtyard at night"></div>
    <div class="body"><h3>Carols in the Courtyard 2019</h3><div class="date"><i></i>18 December,2020</div><p>Joy came to the city of Perth as once again we joined</p></div>
  </article>
  <article class="card" style="left:443px">
    <div class="img" style="background:linear-gradient(180deg,#7fb0e0,#3a6fb0 60%,#2a4f8a)" role="img" aria-label="Group of walkers in blue shirts outdoors"></div>
    <div class="body"><h3>Walk My Way – Rockingham</h3><div class="date"><i></i>18 December,2020</div><p>Joy came to the city of Perth as once again we joined</p></div>
  </article>
  <article class="card" style="left:786px">
    <div class="img" style="background:linear-gradient(180deg,#2f4a2a,#6a8a4a 55%,#8a3a2a)" role="img" aria-label="Christmas wreath decoration"></div>
    <div class="body"><h3>Carols in the Courtyard 2019</h3><div class="date"><i></i>18 December,2020</div><p>Joy came to the city of Perth as once again we joined</p></div>
  </article>
</section>

<footer class="footer">
  <div class="fcol" style="left:99px">
    <div class="fbrand"><span></span>Calverin Church</div>
    <div class="small">Lorem ipsum dolor sit onsectetur adipiscing elit, sed do em tempor incididunt ut labore et dolore magna aliqua.</div>
    <div class="fsocial"><i></i><i></i><i></i></div>
  </div>
  <div class="fcol" style="left:355px">
    <h4>Quick Links</h4>
    <a>Home</a><a>Sermons</a><a>About Us</a><a>Achurch Life</a><a>News</a><a>Weddings</a><a>Contact Us</a>
  </div>
  <div class="fcol" style="left:542px">
    <h4>Contact Us</h4>
    <div>⌖ 42 Harlow Street<br>&nbsp;&nbsp;&nbsp;Perth, WA 6000</div>
    <div>☏ 08 9000 4417</div>
    <div>✉ office@stmarensperth.org.au</div>
    <div>◷ Office Hours:<br>&nbsp;&nbsp;&nbsp;Tuesday, Thursday &amp; Friday:<br>&nbsp;&nbsp;&nbsp;9am-4pm</div>
  </div>
  <div class="fcol" style="left:847px">
    <h4>Subscribe for Newsletter</h4>
    <div class="input">Email Address</div>
    <div class="submit">SUBMIT</div>
  </div>
  <div class="fline"></div>
  <div class="copyright">© 2020 St Maren’s Perth Calverin Church. All Rights Reserved.</div>
</footer>

</body>
</html>
```